Fernleigh Drafting - Flyer Design

I'm looking for good designs of the 2 sided flyer size DL (210 x 95 mm)
Please make sure the design is in the same colours as my business card. Image attached.
Include Architectural plan at the background.
Please note that some words are in capital letters...
FRONT PAGE including :
Are you planning to RENOVATE, EXTEND the house, build new GRANNY FLAT?
Do you need assistance with DA , COMPLYING DEVELOPMENT?
Is your building budget tight and you DON'T WANT to spend it on the ARCHITECTURAL FEES?
For free obligation quote contact:
FERNLEIGH DRAFTING
fernleighdrafting@mailvane.com.au
Dorota - 0491 827 604
For more details check: www.fernleighdrafting.com.au
Follow us on facebook: www.socialvine.com/fernleighdrafting
BACK PAGE including:
Services
- Building Design
- Architectural Drafting
- 3D Modelling
- Terval Assessment
- Building Specifications
- Council Submission Services
- Coordination with Building Professionals
Contact Dorota on 0491 827 604 or fernleighdrafting@mailvane.com.au for obligation free quote

```html
<!DOCTYPE html>
<html lang="en">
<head>
<meta charset="utf-8">
<title>Fernleigh Drafting – DL Flyer</title>
<link rel="stylesheet" href="https://fonts.googleapis.com/css2?family=Montserrat:wght@400;500;600;700&display=swap">
<style>
  :root {
    --page-bg: #e9e6e1;
    --paper: #ffffff;
    --brand-blue: #1ba3dc;
    --soft-blue: #7eaadb;
    --deep-blue: #1f5fae;
    --band-grey: #8b8d90;
    --ink: #2f2f31;
    --sketch-light: #f4f5f6;
    --sketch-mid: #c9ccd0;
    --plan-light: #f7f9fb;
    --plan-mid: #d6dde5;
  }
  * { box-sizing: border-box; margin: 0; padding: 0; }
  html, body { width: 1099px; height: 1200px; overflow: hidden; }
  body {
    background: var(--page-bg);
    font-family: "Montserrat", Arial, sans-serif;
    color: var(--ink);
    position: relative;
  }
  .flyer {
    position: absolute;
    top: 66px;
    width: 500px;
    height: 1068px;
    background: var(--paper);
    overflow: hidden;
    box-shadow: 0 4px 14px rgba(0,0,0,0.25);
  }
  .flyer--front { left: 50px; }
  .flyer--back { left: 569px; }

  .flyer__art {
    position: absolute;
    left: 0; top: 0;
    width: 500px; height: 420px;
  }
  .flyer__bands {
    position: absolute;
    left: 0; top: 0;
    width: 500px; height: 1068px;
  }

  .pitch {
    position: absolute;
    top: 440px; left: 0; width: 500px;
    text-align: center;
    font-size: 23px;
    line-height: 34px;
    font-weight: 400;
  }
  .pitch p { margin-bottom: 14px; }
  .pitch strong {
    color: var(--brand-blue);
    font-weight: 600;
    font-size: 25px;
    letter-spacing: 0.5px;
  }

  .services {
    position: absolute;
    top: 430px; left: 0; width: 500px;
    text-align: center;
    font-size: 23px;
    line-height: 34px;
    letter-spacing: 0.4px;
  }
  .services h2 {
    font-size: 23px;
    font-weight: 700;
    line-height: 34px;
  }
  .services ul { list-style: none; }
  .services li::before { content: "• "; }
  .services li.two-line { line-height: 30px; }

  .contact {
    position: absolute;
    left: 0; width: 500px;
    top: 800px;
    text-align: center;
    color: #fff;
  }
  .contact__lead {
    font-size: 16px;
    font-weight: 400;
  }
  .contact__brand {
    margin: 8px 0 14px;
    font-size: 38px;
    line-height: 40px;
    font-weight: 700;
    color: #fff;
  }
  .contact__details {
    font-size: 22px;
    line-height: 30px;
    font-weight: 400;
  }
</style>
</head>
<body>

<section class="flyer flyer--front" aria-label="Flyer front">
  <svg class="flyer__art" viewBox="0 0 500 420" role="img" aria-label="Pencil sketch of a weatherboard house extension with deck and stairs">
    <defs>
      <linearGradient id="sketchTone" x1="0" y1="0" x2="1" y2="1">
        <stop offset="0" stop-color="var(--sketch-light)"/>
        <stop offset="1" stop-color="var(--sketch-mid)"/>
      </linearGradient>
    </defs>
    <rect width="500" height="420" fill="url(#sketchTone)"/>
  </svg>
  <svg class="flyer__bands" viewBox="0 0 500 1068" aria-hidden="true">
    <path d="M0 388 Q220 420 500 352 V420 H0 Z" fill="var(--paper)"/>
    <path d="M0 380 Q230 405 500 346 L500 360 Q250 415 0 392 Z" fill="var(--deep-blue)"/>
    <path d="M120 406 Q320 395 500 358 L500 414 Q330 398 120 406 Z" fill="var(--band-grey)"/>
    <path d="M0 770 Q250 745 500 800 V1068 H0 Z" fill="var(--band-grey)"/>
    <path d="M0 786 Q250 765 500 818 V1068 H0 Z" fill="var(--soft-blue)"/>
    <path d="M0 808 Q220 778 500 842 V1068 H0 Z" fill="var(--brand-blue)"/>
    <rect x="0" y="842" width="500" height="226" fill="var(--brand-blue)"/>
  </svg>

  <div class="pitch">
    <p>Are you planning to <strong>RENOVATE,</strong><br><strong>EXTEND</strong> the house, build new<br><strong>GRANNY FLAT?</strong></p>
    <p>Do you need assistance with <strong>DA ,</strong><br><strong>COMPLYING DEVELOPMENT?</strong></p>
    <p>Is your building budget tight and you<br><strong>DON'T WANT</strong> to spend it on the<br><strong>ARCHITECTURAL FEES?</strong></p>
  </div>

  <div class="contact">
    <p class="contact__lead">For free obligation quote contact:</p>
    <p class="contact__brand">Fernleigh<br>Drafting</p>
    <div class="contact__details">
      <p>fernleighdrafting@mailvane.com.au</p>
      <p>Dorota - 0491 827 604</p>
      <p>www.fernleighdrafting.com.au</p>
      <p>Socialvine : fernleighdrafting</p>
    </div>
  </div>
</section>

<section class="flyer flyer--back" aria-label="Flyer back">
  <svg class="flyer__art" viewBox="0 0 500 420" role="img" aria-label="Rolled architectural floor plans over a house plan drawing">
    <defs>
      <linearGradient id="planTone" x1="0" y1="0" x2="1" y2="1">
        <stop offset="0" stop-color="var(--plan-light)"/>
        <stop offset="1" stop-color="var(--plan-mid)"/>
      </linearGradient>
    </defs>
    <rect width="500" height="420" fill="url(#planTone)"/>
  </svg>
  <svg class="flyer__bands" viewBox="0 0 500 1068" aria-hidden="true">
    <path d="M0 388 Q220 420 500 352 V420 H0 Z" fill="var(--paper)"/>
    <path d="M0 380 Q230 405 500 346 L500 360 Q250 415 0 392 Z" fill="var(--deep-blue)"/>
    <path d="M120 406 Q320 395 500 358 L500 414 Q330 398 120 406 Z" fill="var(--band-grey)"/>
    <path d="M0 770 Q250 745 500 800 V1068 H0 Z" fill="var(--band-grey)"/>
    <path d="M0 786 Q250 765 500 818 V1068 H0 Z" fill="var(--soft-blue)"/>
    <path d="M0 808 Q220 778 500 842 V1068 H0 Z" fill="var(--brand-blue)"/>
    <rect x="0" y="842" width="500" height="226" fill="var(--brand-blue)"/>
  </svg>

  <div class="services">
    <h2>Services</h2>
    <ul>
      <li>Building Design</li>
      <li>Architectural Drafting</li>
      <li>3D Modelling</li>
      <li>Terval Assessment</li>
      <li>Building Specifications</li>
      <li>Council Submission Services</li>
      <li class="two-line">Coordination with Building<br>Professionals</li>
    </ul>
  </div>

  <div class="contact">
    <p class="contact__lead">For free obligation quote contact:</p>
    <p class="contact__brand">Fernleigh<br>Drafting</p>
    <div class="contact__details">
      <p>fernleighdrafting@mailvane.com.au</p>
      <p>Dorota - 0491 827 604</p>
      <p>www.fernleighdrafting.com.au</p>
      <p>Socialvine : fernleighdrafting</p>
    </div>
  </div>
</section>

</body>
</html>
```